Tinker's Fox sports bar beer & food menu

We need a menu design for our gastropub sports bar in L.A.'s Sawtelle Neighborhood (Little Osaka). We have a full-bar (hard liquor, craft beer, wine and cocktails) . We have a lunch and dinner menu as well as a happy hour menu. On Sundays we have a seperate menu with brunch items. The design concept is a British pub type of sports bar. We're looking for something different from our existing menu design. Ideally something cleaner and more legible. It should mesh a simple, modern sensibility with the more traditional darkened pub style of our interior design.

You can check out our Venuvista page for photos of the interior/exterior:
https://www.venuvista.com/biz_photos/tinkers-fox-los-angeles?tab=interior

You can view our existing menu here:
https://www.venuvista.com/biz_photos/tinkers-fox-los-angeles?tab=menu

If there's an area of the design that can be a little more playful it's our highlighted event schedule so that the events will stand out.

Target Market(s)

Age of 25 and up. Sawtelle is a cultural hub that caters to a younger, moderately affluent crowd.

Industry/Entity Type

Sports Bar

Font styles to use
Sans Serif

Colors

Designer to choose colors to be used in the design.

Requirements
Must have
• Logo, highlighted event schedule (beer pong Monday, trivia Tuesday, taco Tuesday, whiskey Wednesday, karaoke Saturday). The menu should be easy to read in a darkened bar. We'll be printing on standard 8.5x11 in portrait.
Nice to have
• We're trying to have the menu take up as few pages as possible.
Should not have
• We're trying to have the menu take up as few pages as possible. Food photography isn't necessary. A cover isn't necessary. Please avoid clip art of food.

```html
<!DOCTYPE html>
<html lang="en">
<head>
<meta charset="utf-8">
<title>Tinker's Fox Menu</title>
<link href="https://fonts.googleapis.com/css2?family=Archivo:ital,wght@0,400;0,500;0,600;1,400&display=swap" rel="stylesheet">
<style>
:root{
  --backdrop:#cfcdcd;
  --paper:#f6e4cf;
  --paper-glow:#fdf6ec;
  --ink:#231a14;
  --ink-soft:#3b2e25;
  --bar-light:#caa28b;
  --bar-dark:#7a4f3e;
  --bar-text:#fff8f0;
  --logo:#2a1d15;
  --amber:#e9a21f;
  --frame-a:#ef9f8a;
  --frame-b:#f3d77a;
  --frame-c:#93bde0;
}
*{margin:0;padding:0;box-sizing:border-box}
html,body{width:1200px;height:1015px;overflow:hidden;background:var(--backdrop)}
body{font-family:"Archivo",sans-serif;color:var(--ink)}
.stage{position:relative;width:1300px;height:1100px;transform:scale(0.923077);transform-origin:0 0}
.page{position:absolute;top:112px;width:620px;height:875px;
  background:radial-gradient(ellipse at 50% 45%,var(--paper-glow) 0%,var(--paper) 75%);
  box-shadow:3px 5px 10px rgba(0,0,0,.28)}
.page--left{left:24px}
.page--right{left:656px}
.frame{position:absolute;left:14px;top:14px;right:14px;bottom:14px;
  border:7px solid transparent;
  border-image:linear-gradient(135deg,var(--frame-a),var(--frame-b),var(--frame-c),var(--frame-a)) 1}
.brand{position:absolute;left:0;right:0;top:44px;display:flex;justify-content:center;align-items:center;gap:10px}
.brand__mark{width:30px;height:30px;border-radius:50%;background:var(--amber)}
.brand__text{display:flex;flex-direction:column;align-items:center}
.brand__name{font-size:34px;font-weight:600;color:var(--logo);line-height:1}
.brand__tag{font-size:7px;letter-spacing:3px;color:var(--logo);margin-top:3px}
.section-bar{position:absolute;left:210px;width:200px;height:19px;
  background:linear-gradient(90deg,var(--bar-light),var(--bar-dark));
  color:var(--bar-text);font-size:12.5px;font-weight:500;text-align:center;line-height:19px;letter-spacing:.2px}
.items{position:absolute;left:58px;width:512px;list-style:none}
.page--right .items{left:57px}
.item{position:relative;margin-bottom:8px}
.item--tight{margin-bottom:6px}
.item__name{font-size:11.5px;font-weight:500;line-height:13px;display:block}
.item__price{position:absolute;right:0;top:0;font-size:12px;font-weight:500;line-height:13px}
.item__desc{display:block;font-size:8px;font-style:italic;line-height:10px;color:var(--ink-soft);margin-left:8px;max-width:290px}
.items--plain .item{margin-bottom:5px}
.divider{position:absolute;height:0;border-top:1.3px dotted var(--ink)}
.events{position:absolute;height:15px;background:var(--bar-dark);color:var(--bar-text);
  font-size:10px;font-weight:600;letter-spacing:.7px;line-height:15px;text-align:center;white-space:nowrap}
</style>
</head>
<body>
<div class="stage">

  <!-- Page one -->
  <section class="page page--left">
    <div class="frame" role="img" aria-label="Decorative border of small coloured triangles"></div>
    <header class="brand">
      <span class="brand__mark"></span>
      <div class="brand__text"><span class="brand__name">Tinker's Fox</span><span class="brand__tag">PUB &amp; RESTAURANT</span></div>
    </header>

    <h2 class="section-bar" style="top:122px">BURGERS AND SANDWICHES</h2>
    <ul class="items" style="top:151px">
      <li class="item"><span class="item__name">Chicken Sandwich</span><span class="item__price">$12</span><span class="item__desc">Chicken Breast, Applewood Bacon, Butter Lettuce, White Cheddar, Avocado and Tomato Served on Sourdough Bread</span></li>
      <li class="item"><span class="item__name">Buttermilk Fried Chicken</span><span class="item__price">$13</span><span class="item__desc">Coleslaw, Provolone, Tomato, and a Spiced Mayonnaise on a Pretzel Roll</span></li>
      <li class="item"><span class="item__name">Short Rib Sandwich</span><span class="item__price">$13</span><span class="item__desc">Beef Shorts, Mayo, Tomato, Caramelized Onions, Arugula, Pepper Jack Cheese Served on Sourdough Bread</span></li>
      <li class="item"><span class="item__name">Grilled Cheese Sandwich</span><span class="item__price">$13</span><span class="item__desc">Cheese, Provolone and Cheddar Cheese</span></li>
      <li class="item"><span class="item__name">Tinker's Fox Burger</span><span class="item__price">$14</span><span class="item__desc">Sharp Cheddar, Arugula, Roasted Shallots, Bacon Jam with Malt Aioli</span></li>
      <li class="item"><span class="item__name">The Truffle Burger</span><span class="item__price">$15</span><span class="item__desc">Caramelized Onions, Arugula, Truffle Pecorino, Truffle Mayo and Truffle Fries</span></li>
      <li class="item"><span class="item__name">The Sloppy Joe</span><span class="item__price">$10</span><span class="item__desc">Shredded Lettuce and Sharp Cheddar</span></li>
      <li class="item"><span class="item__name">Veggie Burger</span><span class="item__price">$12</span><span class="item__desc">Concoction of kale, Tomato, Avocado, Sharp Cheddar with a Balsamic Reduction</span></li>
      <li class="item" style="margin-bottom:11px"><span class="item__name">Flat Iron Steak Sandwich</span><span class="item__price">$16</span><span class="item__desc">Arugula, Peppers, Fontina, Onion and Mayo</span></li>
      <li class="item"><span class="item__name">Chicken Spinach Wrap</span><span class="item__price">$10</span><span class="item__desc">Chicken, Bacon, Lettuce, Tomato, Avocado, Ranch and Mayo</span></li>
      <li class="item"><span class="item__name">Fried Chicken Sliders (4)</span><span class="item__price">$12</span><span class="item__desc">Coleslaw, Lime Sriracha Sauce</span></li>
    </ul>

    <div class="divider" style="top:531px;left:42px;width:259px"></div>
    <div class="divider" style="top:531px;left:333px;width:246px"></div>

    <h2 class="section-bar" style="top:544px">BIG DOG BITES</h2>
    <ul class="items" style="top:583px">
      <li class="item"><span class="item__name">Atlantic Cod Fish N' Chips</span><span class="item__price">$15</span><span class="item__desc">House Tartar Sauce, Vinegar and Lemon Wedge</span></li>
      <li class="item"><span class="item__name">Oven Roasted ½ Roasted Chicken</span><span class="item__price">$16</span><span class="item__desc">Boneless Chicken, Broccolini, Fingerling Potatoes, Topped with Chimichurri Sauce</span></li>
      <li class="item"><span class="item__name">Black Mussels</span><span class="item__price">$17</span><span class="item__desc">Tequila Chipotle Sauce, Cilantro and Cherry Tomatoes</span></li>
      <li class="item"><span class="item__name">Flat Iron Steak</span><span class="item__price">$19</span><span class="item__desc">French Fries, Baby Arugula in a Light peppercorn Sauce</span></li>
    </ul>

    <div class="divider" style="top:714px;left:42px;width:259px"></div>
    <div class="divider" style="top:714px;left:333px;width:246px"></div>

    <h2 class="section-bar" style="top:729px">FLATBREADS</h2>
    <ul class="items" style="top:761px">
      <li class="item item--tight"><span class="item__name">Margherita</span><span class="item__price">$12</span><span class="item__desc">Fresh Mozzarella, Roma Tomatoes and Fresh Italian Basil</span></li>
      <li class="item"><span class="item__name">Vegetarian</span><span class="item__price">$13</span><span class="item__desc">Brussel Sprouts, Peppers, Onions, Zucchini, Goat Cheese, Smoked Mozzarella Topped with a Balsamic Reduction</span></li>
    </ul>

    <p class="events" style="top:829px;left:41px;width:539px">•Beer Pong Monday •Trivia Tuesday •Taco Tuesday •Whiskey Wednesday •Karaoke Saturday</p>
  </section>

  <!-- Page two -->
  <section class="page page--right">
    <div class="frame" role="img" aria-label="Decorative border of small coloured triangles"></div>
    <header class="brand">
      <span class="brand__mark"></span>
      <div class="brand__text"><span class="brand__name">Tinker's Fox</span><span class="brand__tag">PUB &amp; RESTAURANT</span></div>
    </header>

    <ul class="items" style="top:120px">
      <li class="item" style="margin-bottom:10px"><span class="item__name">Prosciutto &amp; Arugula</span><span class="item__price">$14</span><span class="item__desc">Red Onion, Parmesan, Mozzarella</span></li>
      <li class="item" style="margin-bottom:9px"><span class="item__name">Portobello &amp; Truffle</span><span class="item__price">$14</span><span class="item__desc">Portobello White Mushroom, Fontina, Drizzled with Truffle Oil</span></li>
      <li class="item" style="margin-bottom:9px"><span class="item__name">Chicken Tikka Masala</span><span class="item__price">$14</span><span class="item__desc">Tandoori Chicken, Fontini and Raita</span></li>
      <li class="item"><span class="item__name">The Tinker's Fox</span><span class="item__price">$15</span><span class="item__desc">Meatballs, Sausage, Chorizo, Mozzarella and Fresen</span></li>
    </ul>

    <div class="divider" style="top:260px;left:42px;width:259px"></div>
    <div class="divider" style="top:260px;left:333px;width:246px"></div>

    <h2 class="section-bar" style="top:279px">FOR THE TABLE</h2>
    <ul class="items" style="top:307px">
      <li class="item" style="margin-bottom:11px"><span class="item__name">Tinker's 3 Whole Wings</span><span class="item__price">$9</span><span class="item__desc">Choice of Dry Rub, Sweet N' Spicy or Buffalo</span></li>
      <li class="item" style="margin-bottom:9px"><span class="item__name">Brussel Sprouts</span><span class="item__price">$8</span><span class="item__desc">Sautéed with Chorizo, Roasted Almonds and Golden Raisins</span></li>
      <li class="item" style="margin-bottom:9px"><span class="item__name">Golden Calamari</span><span class="item__price">$11</span><span class="item__desc">Traditionally Served with Spiced Marinara</span></li>
      <li class="item" style="margin-bottom:9px"><span class="item__name">Shrimp Mac N' Cheese</span><span class="item__price">$12</span><span class="item__desc">Baked with Fontina, Sharp Cheddar and Parmesan</span></li>
      <li class="item" style="margin-bottom:10px"><span class="item__name">S½ Dozen Oysters</span><span class="item__price">$12</span><span class="item__desc">6 Harbor Cove Served with Our Own Mignonette</span></li>
      <li class="item" style="margin-bottom:8px"><span class="item__name">Charcuterie</span><span class="item__price">$15</span><span class="item__desc">Seasonal Meats and Cheese</span></li>
      <li class="item" style="margin-bottom:9px"><span class="item__name">Nachos</span><span class="item__price">$9</span><span class="item__desc">Medley of Black Beans, Pico De Gallo, Cheese, Jalapeno and Sour Cream</span></li>
      <li class="item"><span class="item__name">Mozzarella Cheese Ctick</span><span class="item__price">$9</span></li>
    </ul>

    <div class="divider" style="top:565px;left:42px;width:259px"></div>
    <div class="divider" style="top:565px;left:333px;width:246px"></div>

    <h2 class="section-bar" style="top:584px">SIDES</h2>
    <ul class="items items--plain" style="top:610px">
      <li class="item"><span class="item__name">House Fries</span><span class="item__price">$6</span></li>
      <li class="item"><span class="item__name">Truffle Fries</span><span class="item__price">$7</span></li>
      <li class="item"><span class="item__name">Dry Rub Fries</span><span class="item__price">$6</span></li>
      <li class="item"><span class="item__name">Sweet Potato Fries</span><span class="item__price">$7</span></li>
    </ul>

    <div class="divider" style="top:694px;left:42px;width:259px"></div>
    <div class="divider" style="top:694px;left:333px;width:246px"></div>

    <h2 class="section-bar" style="top:713px">DESSERT</h2>
    <ul class="items items--plain" style="top:739px">
      <li class="item"><span class="item__name">Coco Flan</span><span class="item__price">$9</span></li>
      <li class="item"><span class="item__name">Cheese Cake</span><span class="item__price">$9</span></li>
      <li class="item"><span class="item__name">Peach Tart</span><span class="item__price">$9</span></li>
    </ul>

    <p class="events" style="top:820px;left:47px;width:538px">•Beer Pong Monday •Trivia Tuesday •Taco Tuesday •Whiskey Wednesday •Karaoke Saturday</p>
  </section>

</div>
</body>
</html>
```